Generic fund comparison

We need a power point template to be used for presentation decks and proposals to clients and prospects. We are an independent Registered Investment Advisor in Pittsburgh Pennsylvania.
Our services include family office, alternative investments, investment management, financial planning and consulting.
We would like to see designs that use the color green and grey as they are part of our logo and brand image. The final design should communicate our guiding principles: 'educate, plan, implement, adapt'

```html
<!DOCTYPE html>
<html lang="en">
<head>
<meta charset="utf-8">
<title>Fennwick – Client Presentation Template</title>
<link rel="stylesheet" href="https://fonts.googleapis.com/css2?family=Raleway:wght@800;900&family=Roboto:wght@400;500;700&display=swap">
<style>
  :root{
    --green:#8dc63f;
    --green-dark:#5b8a2b;
    --grey-dark:#4a4a4a;
    --grey-mid:#6b6b6b;
    --ink:#1f1f1f;
    --body:#707070;
    --panel:#f2f2f2;
    --panel-dark:#e3e3e3;
    --header:#d2d2d2;
    --circle:#e9e9e9;
  }
  html,body{margin:0;padding:0}
  body{width:1200px;height:3708px;overflow:hidden;background:#fff;position:relative;font-family:'Roboto',sans-serif}
  .slide{position:absolute;left:164px;width:608px;height:343px;transform:scale(1.4507);transform-origin:0 0;background:#fff;box-shadow:0 0 1.6px rgba(0,0,0,.38);overflow:hidden}
  .slide svg.layer{position:absolute;left:0;top:0;width:608px;height:343px}
  .s1{top:99px}.s2{top:696px}.s3{top:1293px}.s4{top:1889px}.s5{top:2486px}.s6{top:3082px}
  .brand-name{font-family:'Roboto',sans-serif;font-weight:400;fill:#6a6a6a;letter-spacing:.9px}
  .heading{font-family:'Raleway',sans-serif;font-weight:900;fill:var(--ink)}
  .cover-title{font-family:'Roboto',sans-serif;font-weight:500;font-size:11.6px;fill:#111}
  .band-text{font-family:'Roboto',sans-serif;font-weight:500;font-size:11.5px;fill:#fff}
  .welcome-copy{position:absolute;left:280px;top:97px;width:303px;margin:0;font-size:7.4px;line-height:15.2px;color:var(--body);text-align:justify}
  .welcome-copy p{margin:0 0 9.5px}
  .services-intro{position:absolute;left:207px;top:89px;width:194px;margin:0;font-size:7.3px;line-height:13px;color:var(--body);text-align:justify;text-align-last:center}
  .svc-title{font-family:'Roboto',sans-serif;font-weight:500;font-size:7.4px;fill:#fff}
  .svc-text{font-family:'Roboto',sans-serif;font-size:5.3px;fill:#fff}
  .tbl-head{font-size:5.6px;font-weight:500;fill:#222}
  .tbl-year{font-size:5.6px;font-weight:700;fill:#222}
  .tbl-val{font-size:5.4px;fill:#333}
  .axis{font-size:5.4px;fill:#444}
  .pt-label{font-size:5.4px;fill:#222;font-weight:500}
  .note{font-size:3.8px;fill:#888}
  .disclaimer-head{font-size:7px;fill:#222}
  .disclaimer{position:absolute;left:17px;top:248px;width:574px;margin:0;font-size:4.1px;line-height:7.6px;color:#888;text-align:justify;text-align-last:center}
</style>
</head>
<body>

<svg width="0" height="0" style="position:absolute">
  <defs>
    <radialGradient id="netTL" cx="0" cy="0" r="1">
      <stop offset="0" stop-color="#b7dd6f" stop-opacity=".75"/>
      <stop offset=".6" stop-color="#d6ecb0" stop-opacity=".35"/>
      <stop offset="1" stop-color="#ffffff" stop-opacity="0"/>
    </radialGradient>
    <radialGradient id="netTR" cx="1" cy="0" r="1">
      <stop offset="0" stop-color="#b7dd6f" stop-opacity=".75"/>
      <stop offset=".6" stop-color="#d6ecb0" stop-opacity=".35"/>
      <stop offset="1" stop-color="#ffffff" stop-opacity="0"/>
    </radialGradient>
    <linearGradient id="greenFace" x1="0" y1="0" x2="0" y2="1">
      <stop offset="0" stop-color="#8dc63f"/>
      <stop offset="1" stop-color="#5b8a2b"/>
    </linearGradient>
    <linearGradient id="greyFace" x1="0" y1="0" x2="0" y2="1">
      <stop offset="0" stop-color="#707070"/>
      <stop offset="1" stop-color="#484848"/>
    </linearGradient>
    <linearGradient id="photoTone" x1="0" y1="0" x2="1" y2="1">
      <stop offset="0" stop-color="#cfd6de"/>
      <stop offset=".5" stop-color="#7f8a96"/>
      <stop offset="1" stop-color="#3f5f8c"/>
    </linearGradient>
  </defs>
</svg>

<!-- Cover -->
<section class="slide s1">
  <svg class="layer" viewBox="0 0 608 343">
    <rect x="0" y="0" width="190" height="115" fill="url(#netTL)" role="img" aria-label="Green network-of-dots decoration"/>
    <rect x="418" y="0" width="190" height="115" fill="url(#netTR)" role="img" aria-label="Green network-of-dots decoration"/>
    <rect x="293" y="98" width="20" height="20" fill="var(--green)"/>
    <text class="brand-name" x="304" y="138" font-size="9.5" text-anchor="middle">FENNWICK</text>
    <text class="cover-title" x="304" y="173" text-anchor="middle">INDEPENDENT FINANCIAL ADVISORY SERVICES</text>
    <text class="cover-title" x="304" y="191" text-anchor="middle">TAILORED TO YOUR GOALS</text>
    <rect x="0" y="214" width="608" height="33" fill="var(--green)"/>
    <text class="band-text" x="304" y="234.5" text-anchor="middle">ABC, XYZ – APRIL 2021</text>
  </svg>
</section>

<!-- Welcome -->
<section class="slide s2">
  <svg class="layer" viewBox="0 0 608 343">
    <rect x="0" y="0" width="260" height="343" fill="url(#photoTone)" role="img" aria-label="Photo of an advisor's hands reviewing printed financial charts with a pen"/>
    <rect x="440" y="0" width="168" height="90" fill="url(#netTR)" role="img" aria-label="Green network-of-dots decoration"/>
    <text class="heading" x="280" y="65" font-size="15">WELCOME TO FENNWICK</text>
    <rect x="280" y="81" width="33" height="2" fill="var(--green)"/>
    <rect x="554" y="313" width="12" height="12" fill="var(--green)"/>
    <text class="brand-name" x="560" y="337" font-size="6.6" text-anchor="middle">FENNWICK</text>
  </svg>
  <div class="welcome-copy">
    <p>Lorem ipsum dolor sit amet, consectetur adipiscing elit, sed do eiusmod tempor incididunt ut labore et dolore magna aliqua. Ut enim ad minim veniam, quis nostrud exercitation ullamco laboris nisi ut aliquip ex ea commodo consequat. Duis aute irure dolor in reprehenderit in voluptate velit esse cillum dolore eu fugiat nulla pariatur. Excepteur sint occaecat cupidatat non proident, sunt in culpa qui officia deserunt mollit anim id est laborum.</p>
    <p>Lorem ipsum dolor sit amet, consectetur adipiscing elit, sed do eiusmod tempor incididunt ut labore et dolore magna aliqua. Ut enim ad minim veniam, quis nostrud exercitation ullamco laboris nisi ut aliquip ex ea commodo consequat. Duis aute irure dolor in reprehenderit in voluptate velit esse cillum dolore eu fugiat nulla pariatur.</p>
  </div>
</section>

<!-- Services -->
<section class="slide s3">
  <svg class="layer" viewBox="0 0 608 343">
    <circle cx="304" cy="79" r="120" fill="var(--circle)"/>
    <text class="heading" x="304" y="54" font-size="15" text-anchor="middle">OUR SERVICES</text>
    <rect x="288" y="71" width="32" height="2" fill="var(--green)"/>

    <polygon points="83,87 165,87 191,159 125,209 59,159" fill="url(#greenFace)"/>
    <text class="svc-title" x="125" y="147" text-anchor="middle">Family Office</text>
    <text class="svc-text" x="125" y="161" text-anchor="middle">Lorem ipsum dolor sit amet,</text>
    <text class="svc-text" x="125" y="169" text-anchor="middle">consectetur adipiscing elit, sed</text>
    <text class="svc-text" x="125" y="177" text-anchor="middle">do eiusmod tempor</text>

    <polygon points="418,159 442,87 522,87 548,159 483,209" fill="url(#greenFace)"/>
    <text class="svc-title" x="483" y="147" text-anchor="middle">Consulting</text>
    <text class="svc-text" x="483" y="161" text-anchor="middle">Lorem ipsum dolor sit amet,</text>
    <text class="svc-text" x="483" y="169" text-anchor="middle">consectetur adipiscing elit, sed</text>
    <text class="svc-text" x="483" y="177" text-anchor="middle">do eiusmod tempor</text>

    <polygon points="195,166 260,214 237,289 153,289 130,214" fill="url(#greyFace)"/>
    <text class="svc-title" x="195" y="229" text-anchor="middle">Alternative Investments</text>
    <text class="svc-text" x="195" y="243" text-anchor="middle">Lorem ipsum dolor sit amet,</text>
    <text class="svc-text" x="195" y="251" text-anchor="middle">consectetur adipiscing elit, sed</text>
    <text class="svc-text" x="195" y="259" text-anchor="middle">do eiusmod tempor</text>

    <polygon points="414,166 478,214 455,289 371,289 349,214" fill="url(#greyFace)"/>
    <text class="svc-title" x="414" y="229" text-anchor="middle">Financial Planning</text>
    <text class="svc-text" x="414" y="243" text-anchor="middle">Lorem ipsum dolor sit amet,</text>
    <text class="svc-text" x="414" y="251" text-anchor="middle">consectetur adipiscing elit, sed</text>
    <text class="svc-text" x="414" y="259" text-anchor="middle">do eiusmod tempor</text>

    <polygon points="262,214 347,214 370,289 305,337 239,289" fill="url(#greenFace)"/>
    <text class="svc-title" x="304" y="270" text-anchor="middle">Investment</text>
    <text class="svc-title" x="304" y="279" text-anchor="middle">Management</text>
    <text class="svc-text" x="304" y="291" text-anchor="middle">Lorem ipsum dolor sit amet,</text>
    <text class="svc-text" x="304" y="299" text-anchor="middle">consectetur adipiscing elit, sed</text>
    <text class="svc-text" x="304" y="307" text-anchor="middle">do eiusmod tempor</text>

    <rect x="554" y="313" width="12" height="12" fill="var(--green)"/>
    <text class="brand-name" x="560" y="337" font-size="6.6" text-anchor="middle">FENNWICK</text>
  </svg>
  <p class="services-intro">Lorem ipsum dolor sit amet, consectetur adipiscing elit, sed do eiusmod tempor incididunt ut labore et dolore magna aliqua. Ut enim ad minim veniam</p>
</section>

<!-- Returns table -->
<section class="slide s4">
  <svg class="layer" viewBox="0 0 608 343">
    <rect x="440" y="0" width="168" height="95" fill="url(#netTR)" role="img" aria-label="Green network-of-dots decoration"/>
    <rect x="0" y="0" width="110" height="80" fill="url(#netTL)" opacity=".5" role="img" aria-label="Green network-of-dots decoration"/>
    <text class="heading" x="21" y="32" font-size="14.6">ABC, XYZ – ANNUAL RETURNS VS BENCHMARK*</text>
    <rect x="21" y="49" width="32" height="2" fill="var(--green)"/>

    <rect x="20" y="69" width="397" height="15" fill="var(--header)"/>
    <rect x="417" y="69" width="105" height="255" fill="var(--panel-dark)"/>
    <rect x="20" y="100" width="397" height="224" fill="var(--panel)"/>
    <text x="96" y="79.5" font-size="5.6" fill="#fff" font-weight="500">ALDER</text>

    <text class="tbl-head" x="106" y="95">60/40 Benchmark</text>
    <text class="tbl-head" x="219" y="95">Harbor Ridge</text>
    <text class="tbl-head" x="330" y="95">Kestrel Composite</text>
    <text class="tbl-head" x="440" y="95">50/50 Hedge Funds</text>

    <g fill="var(--green)">
      <rect x="200" y="164" width="52" height="13"/>
      <rect x="91" y="182.5" width="51" height="13"/>
      <rect x="200" y="182.5" width="52" height="13"/>
      <rect x="91" y="237.5" width="51" height="13"/>
    </g>

    <g class="tbl-year">
      <text x="30" y="118">2011</text><text x="30" y="136.4">2012</text><text x="30" y="154.8">2013</text>
      <text x="30" y="173.2">2014</text><text x="30" y="191.6">2015</text><text x="30" y="210">2016</text>
      <text x="30" y="228.4">2017</text><text x="30" y="246.8">2018</text><text x="30" y="265.2">2019</text>
      <text x="30" y="283.6">2020</text><text x="30" y="302">YTD 2021</text>
    </g>
    <g class="tbl-val">
      <text x="108" y="118">0.6%</text><text x="221" y="118">4.6%</text><text x="332" y="118">4.8%</text><text x="443" y="118">4.7%</text>
      <text x="108" y="136.4">11.3%</text><text x="221" y="136.4">10.5%</text><text x="332" y="136.4">14.5%</text><text x="443" y="136.4">12.5%</text>
      <text x="108" y="154.8">16.0%</text><text x="221" y="154.8">8.2%</text><text x="332" y="154.8">12.3%</text><text x="443" y="154.8">10.2%</text>
      <text x="108" y="173.2">6.1%</text><text x="221" y="173.2">-2.5%</text><text x="332" y="173.2">15.5%</text><text x="443" y="173.2">6.5%</text>
      <text x="108" y="191.6">-0.1%</text><text x="221" y="191.6">-1.7%</text><text x="332" y="191.6">14.6%</text><text x="443" y="191.6">6.5%</text>
      <text x="108" y="210">7.2%</text><text x="221" y="210">4.6%</text><text x="332" y="210">5.7%</text><text x="443" y="210">5.2%</text>
      <text x="108" y="228.4">13.9%</text><text x="221" y="228.4">9.2%</text><text x="332" y="228.4">10.4%</text><text x="443" y="228.4">9.8%</text>
      <text x="108" y="246.8">-3.8%</text><text x="221" y="246.8">6.6%</text><text x="332" y="246.8">11.3%</text><text x="443" y="246.8">9.0%</text>
      <text x="108" y="265.2">19.3%</text><text x="221" y="265.2">7.7%</text><text x="332" y="265.2">10.7%</text><text x="443" y="265.2">9.2%</text>
      <text x="108" y="283.6">12.1%</text><text x="221" y="283.6">15.8%</text><text x="332" y="283.6">19.6%</text><text x="443" y="283.6">17.7%</text>
      <text x="108" y="302">2.5%</text><text x="221" y="302">8.2%</text><text x="332" y="302">5.1%</text><text x="443" y="302">6.7%</text>
    </g>
    <text class="note" x="20" y="336">Benchmark = 45% xxxxxxxx, 15% yyyyyyyy, 40% zzzzzzzz</text>

    <rect x="554" y="313" width="12" height="12" fill="var(--green)"/>
    <text class="brand-name" x="560" y="337" font-size="6.6" text-anchor="middle">FENNWICK</text>
  </svg>
</section>

<!-- Risk / return scatter -->
<section class="slide s5">
  <svg class="layer" viewBox="0 0 608 343">
    <rect x="440" y="0" width="168" height="95" fill="url(#netTR)" role="img" aria-label="Green network-of-dots decoration"/>
    <rect x="0" y="0" width="110" height="80" fill="url(#netTL)" opacity=".5" role="img" aria-label="Green network-of-dots decoration"/>
    <text class="heading" x="21" y="32" font-size="14.6">ABC, XYZ – ANNUAL RETURNS VS BENCHMARK*</text>
    <rect x="288" y="49" width="32" height="2" fill="var(--green)"/>

    <g stroke="#cfcfcf" stroke-width=".6">
      <line x1="52" y1="64" x2="557" y2="64"/><line x1="52" y1="95" x2="557" y2="95"/>
      <line x1="52" y1="126" x2="557" y2="126"/><line x1="52" y1="157" x2="557" y2="157"/>
      <line x1="52" y1="187" x2="557" y2="187"/><line x1="52" y1="219" x2="557" y2="219"/>
      <line x1="52" y1="250" x2="557" y2="250"/><line x1="52" y1="281" x2="557" y2="281"/>
      <line x1="52" y1="309" x2="557" y2="309"/>
      <line x1="52" y1="64" x2="52" y2="309"/><line x1="115" y1="64" x2="115" y2="309"/>
      <line x1="178" y1="64" x2="178" y2="309"/><line x1="241" y1="64" x2="241" y2="309"/>
      <line x1="304" y1="64" x2="304" y2="309"/><line x1="367" y1="64" x2="367" y2="309"/>
      <line x1="430" y1="64" x2="430" y2="309"/><line x1="493" y1="64" x2="493" y2="309"/>
      <line x1="557" y1="64" x2="557" y2="309"/>
    </g>
    <g class="axis" text-anchor="end">
      <text x="50" y="66">16.0%</text><text x="50" y="97">14.0%</text><text x="50" y="128">12.0%</text>
      <text x="50" y="159">10.0%</text><text x="50" y="189">8.0%</text><text x="50" y="221">6.0%</text>
      <text x="50" y="252">4.0%</text><text x="50" y="283">2.0%</text><text x="50" y="311">0.0%</text>
    </g>
    <g class="axis" text-anchor="middle">
      <text x="79" y="321">2.0%</text><text x="146" y="321">4.0%</text><text x="209" y="321">6.0%</text>
      <text x="272" y="321">8.0%</text><text x="334" y="321">10.0%</text><text x="397" y="321">12.0%</text>
      <text x="461" y="321">14.0%</text><text x="529" y="321">16.0%</text>
      <text x="304" y="335">Standard Deviation</text>
      <text transform="translate(17 167) rotate(90)">Return</text>
    </g>
    <g fill="var(--green)">
      <circle cx="491" cy="95" r="2.2"/><circle cx="178" cy="123" r="2.2"/>
      <circle cx="124" cy="174" r="2.2"/><circle cx="292" cy="184" r="2.2"/>
      <circle cx="156" cy="209" r="2.2"/><circle cx="529" cy="266" r="2.2"/>
      <circle cx="121" cy="304" r="2.2"/>
    </g>
    <g class="pt-label">
      <text x="496" y="93">Total Market 3000</text>
      <text x="183" y="121">Kestrel</text>
      <text x="129" y="172">Hedge Funds 50/50</text>
      <text x="297" y="182">60/40 Benchmark</text>
      <text x="161" y="207">Harbor Ridge</text>
      <text x="534" y="264">Global ex US</text>
      <text x="126" y="301">Govt/Credit bonds Index</text>
    </g>

    <rect x="577" y="313" width="12" height="12" fill="var(--green)"/>
    <text class="brand-name" x="583" y="339" font-size="6.6" text-anchor="middle">FENNWICK</text>
  </svg>
</section>

<!-- Closing -->
<section class="slide s6">
  <svg class="layer" viewBox="0 0 608 343">
    <rect x="0" y="0" width="190" height="115" fill="url(#netTL)" role="img" aria-label="Green network-of-dots decoration"/>
    <rect x="418" y="0" width="190" height="115" fill="url(#netTR)" role="img" aria-label="Green network-of-dots decoration"/>
    <rect x="293" y="92" width="20" height="20" fill="var(--green)"/>
    <text class="brand-name" x="304" y="132" font-size="9.5" text-anchor="middle">FENNWICK</text>
    <rect x="0" y="151" width="608" height="33" fill="var(--green)"/>
    <text x="304" y="174.5" font-family="Raleway, sans-serif" font-weight="900" font-size="18" fill="#fff" text-anchor="middle">THANK YOU</text>
    <text class="disclaimer-head" x="304" y="240" text-anchor="middle">DISCLAIMER</text>
  </svg>
  <p class="disclaimer">Disclaimer: this document is a general communication being provided for informational purposes only. It is educational in nature and not designed to be taken as advice or a recommendation for any specific investment product, strategy, plan feature or other purpose in any jurisdiction. Any examples used are generic, hypothetical and for illustration purposes only. This material does not contain sufficient information to support an investment decision and it should not be relied upon by you in evaluating the merits of investing in any securities or products. In addition, users should make an independent assessment of the legal, regulatory, tax, credit, and accounting implications and determine, together with their own professional advisers, if any investment mentioned herein is believed to be suitable to their personal goals. Investors should ensure that they obtain all available relevant information before making any investment. Any forecasts, figures, opinions or investment techniques and strategies set out are for information purposes only, based on certain assumptions and current market conditions and are subject to change without prior notice. All information presented herein is considered to be accurate at the time of production, but no warranty of accuracy is given and no liability in respect of any error or omission is accepted. It should be noted that investment involves risks, the value of investments and the income from them may fluctuate in accordance with market conditions and taxation agreements and investors may not get back the full amount invested. Both past performance and yields are not reliable indicators of current and future results.</p>
</section>

</body>
</html>
```